Redesign Comparisson chart - make modern and effective

Use your imaginations to make a powerful distinction between KRV & other holistic modalities. There are 7 elements physical, mental, emotional, energetic, subconscious, superconscious and before and after testing.
We want it to be obvious that KRV is the only modality that works on all these elements simultaneously. We do not want to include any chakras as we want this information to be accepted by a wide range of people and belief systems.'

We want it to look simple but effective. Professional but powerful. We want KRV to stand out even of you eye just passed over i.
Updates

Hi everyone, thanks for your submissions so far. Basically what this image is meant to represent is a comparison chart between all the modalities There are 5 elements physical, mental, emotional, subconscious and superconscious. we want to reflect that KRV is the only modality that works on all these elements simultaneously. As we want the concept to be accepted and not considered woo woo, we want to steer away from chakras.

Target Market(s)

Professionals

Industry/Entity Type

Professional services

Font styles to use
Sans Serif
Other font styles liked:
• Poppins Monserratt

Colors
0094D4
00A9DD
6FCCEA
C7EBF8
E9F6FB

Requirements
Must have
• Clear/professional and clean look. Brand colours and logos. All typography and formats must be cohesive.
Nice to have
• More easy to read, different layout
Should not have
• Do not change the data just the way its presented. No chakras

```html
<!DOCTYPE html>
<html lang="en">
<head>
<meta charset="utf-8">
<title>Choose KRV – Modality Comparison Chart</title>
<link rel="stylesheet" href="https://fonts.googleapis.com/css2?family=Montserrat:wght@400;500;600;700;800&family=Poppins:wght@400;500;600&display=swap">
<style>
:root{
  --brand:#29abe2;
  --brand-deep:#0094d4;
  --brand-mid:#00a9dd;
  --brand-light:#6fccea;
  --brand-pale:#c7ebf8;
  --brand-mist:#e9f6fb;
  --ink:#3a3a3a;
  --muted:#5a5a5a;
  --label-bg:#efefef;
  --rule:#e4e4e4;
  --physical:#d32f34;
  --mental:#3b9bd8;
  --emotional:#3cae4a;
  --energetic:#f39322;
  --subconscious:#f2d31b;
  --superconscious:#7b68ae;
  --testing:#b56b9e;
}
*{box-sizing:border-box;margin:0;padding:0}
html,body{width:1200px;height:2257px;overflow:hidden;background:#fff}
body{position:relative;font-family:"Montserrat",sans-serif;color:var(--ink)}

.page-title{position:absolute;left:60px;top:80px;font-size:27px;font-weight:800;color:var(--brand);letter-spacing:.2px}
.intro{position:absolute;left:0;top:124px;width:760px;height:72px;padding:8px 0 0 60px;
  background:linear-gradient(90deg,var(--brand-light) 0%,var(--brand-pale) 45%,rgba(233,246,251,0) 100%)}
.intro p{font-size:13.5px;line-height:19px;font-weight:500;color:#1d4f66}

.brand{position:absolute;right:60px;top:146px;font-family:"Montserrat",sans-serif;font-weight:700;font-size:22px;line-height:26px;color:var(--brand);white-space:nowrap}

.band{position:absolute;left:0;top:1530px;width:1200px;height:110px;
  background:linear-gradient(180deg,var(--brand-mid),var(--brand-deep))}

.chart{position:absolute;left:60px;top:232px;width:1084px;height:1396px;background:#fff;border-radius:10px;
  box-shadow:0 4px 18px rgba(0,0,0,.08)}
.col-rules{position:absolute;left:236px;top:60px;display:grid;grid-template-columns:repeat(7,121px)}
.col-rules span{height:1336px;border-left:1px solid var(--rule)}
.grid{position:absolute;left:0;top:0;display:grid;grid-template-columns:236px repeat(7,121px)}
.head{height:60px;display:flex;align-items:center;justify-content:center;text-align:center;
  font-size:11px;font-weight:700;color:#fff;line-height:13px;border-radius:6px 6px 0 0;margin:0 1px}
.h-physical{background:var(--physical)}.h-mental{background:var(--mental)}.h-emotional{background:var(--emotional)}
.h-energetic{background:var(--energetic)}.h-subconscious{background:var(--subconscious)}
.h-superconscious{background:var(--superconscious)}.h-testing{background:var(--testing)}
.spacer{height:6px;grid-column:1/-1}
.label{height:47px;display:flex;align-items:center;justify-content:center;text-align:center;
  font-size:13px;font-weight:600;color:var(--ink);line-height:15px;background:var(--label-bg);
  border-bottom:2px solid #fff;border-radius:4px;margin-right:4px}
.cell{height:47px;display:flex;align-items:center;justify-content:center;border-bottom:1px solid #f3f3f3}
.tick{width:23px;height:23px}
.c-physical{color:var(--physical)}.c-mental{color:var(--mental)}.c-emotional{color:var(--emotional)}
.c-energetic{color:var(--energetic)}.c-subconscious{color:var(--subconscious)}
.c-superconscious{color:var(--superconscious)}.c-testing{color:var(--testing)}

.feature{position:absolute;left:-24px;top:214px;width:1132px;height:92px;border:2px solid var(--brand-deep);
  border-radius:18px;background:#fff;box-shadow:0 6px 16px rgba(0,80,130,.18);
  display:grid;grid-template-columns:258px repeat(7,121px);align-items:center;padding-left:22px}
.feature-label{height:70px;background:var(--brand);border-radius:6px 0 0 6px;display:flex;align-items:center;
  justify-content:center;font-family:"Montserrat",sans-serif;font-weight:700;font-size:38px;color:#fff;margin-right:22px}
.feature .tick{width:32px;height:32px}
.feature .cell{border:none;height:70px}

.notes h3{font-size:13.5px;font-weight:700;letter-spacing:.3px;padding-bottom:6px;margin-bottom:10px;position:relative}
.notes h3::after{content:"";position:absolute;left:0;bottom:0;width:50px;height:2px;background:currentColor}
.notes p{font-family:"Poppins",sans-serif;font-size:14.5px;line-height:20px;color:var(--muted)}
.note{position:absolute;width:490px}
.n-physical h3{color:var(--physical)}.n-mental h3{color:var(--mental)}.n-emotional h3{color:var(--emotional)}
.n-energetic h3{color:var(--energetic)}.n-subconscious h3{color:#e0b400}
.n-superconscious h3{color:var(--superconscious)}.n-testing h3{color:var(--testing)}

.footer{position:absolute;left:0;top:2172px;width:1200px;text-align:center}
.footer-brand{display:inline-flex;align-items:center;gap:8px;font-weight:700;font-size:17px;color:var(--brand)}
.footer-dot{width:18px;height:18px;border-radius:50%;background:var(--brand)}
.footer-url{font-size:14px;font-weight:600;color:#222;margin-top:8px}
</style>
</head>
<body>
<svg width="0" height="0" style="position:absolute">
  <symbol id="tick" viewBox="0 0 24 24">
    <circle cx="12" cy="12" r="10" fill="none" stroke="currentColor" stroke-width="1.6"/>
    <path d="M7.5 12.3l3 3 6-6.3" fill="none" stroke="currentColor" stroke-width="1.8" stroke-linecap="round" stroke-linejoin="round"/>
  </symbol>
</svg>

<h1 class="page-title">CHOOSE KRV FOR FAST, IMMEDIATE AND POWERFUL RESULTS</h1>
<div class="intro">
  <p>I must experience healing on all levels, I am not just a body.</p>
  <p>I want to learn how to heal myself, so I'm not dependent on others.</p>
  <p>I want to release all my emotional and mental blocks, so I can be the best version of myself.</p>
</div>
<div class="brand">Haven Method</div>

<div class="band"></div>

<section class="chart">
  <div class="col-rules"><span></span><span></span><span></span><span></span><span></span><span></span><span></span></div>
  <div class="grid">
    <div></div>
    <div class="head h-physical">PHYSICAL</div><div class="head h-mental">MENTAL</div>
    <div class="head h-emotional">EMOTIONAL</div><div class="head h-energetic">ENERGETIC</div>
    <div class="head h-subconscious">SUB<br>CONSCIOUS</div><div class="head h-superconscious">SUPER<br>CONSCIOUS</div>
    <div class="head h-testing">BEFORE &amp;<br>AFTER TESTING</div>
    <div class="spacer"></div>

    <div class="label">MASSAGE</div><div class="cell c-physical"><svg class="tick"><use href="#tick"/></svg></div><div class="cell"></div><div class="cell"></div><div class="cell"></div><div class="cell"></div><div class="cell"></div><div class="cell"></div>
    <div class="label">YOGA</div><div class="cell c-physical"><svg class="tick"><use href="#tick"/></svg></div><div class="cell"></div><div class="cell"></div><div class="cell"></div><div class="cell"></div><div class="cell"></div><div class="cell"></div>
    <div class="label">CHINESE<br>MEDICINE</div><div class="cell c-physical"><svg class="tick"><use href="#tick"/></svg></div><div class="cell"></div><div class="cell"></div><div class="cell c-energetic"><svg class="tick"><use href="#tick"/></svg></div><div class="cell"></div><div class="cell"></div><div class="cell"></div>

    <div class="spacer" style="height:105px"></div>

    <div class="label">CHIROPRACTIC</div><div class="cell c-physical"><svg class="tick"><use href="#tick"/></svg></div><div class="cell"></div><div class="cell"></div><div class="cell c-energetic"><svg class="tick"><use href="#tick"/></svg></div><div class="cell"></div><div class="cell"></div><div class="cell c-testing"><svg class="tick"><use href="#tick"/></svg></div>
    <div class="label">KINESIOLOGY</div><div class="cell c-physical"><svg class="tick"><use href="#tick"/></svg></div><div class="cell"></div><div class="cell"></div><div class="cell"></div><div class="cell c-subconscious"><svg class="tick"><use href="#tick"/></svg></div><div class="cell"></div><div class="cell c-testing"><svg class="tick"><use href="#tick"/></svg></div>
    <div class="label">NATROPATHY</div><div class="cell c-physical"><svg class="tick"><use href="#tick"/></svg></div><div class="cell"></div><div class="cell"></div><div class="cell"></div><div class="cell"></div><div class="cell"></div><div class="cell"></div>
    <div class="label">NUTRITIONAL<br>HEALING</div><div class="cell c-physical"><svg class="tick"><use href="#tick"/></svg></div><div class="cell"></div><div class="cell"></div><div class="cell"></div><div class="cell"></div><div class="cell"></div><div class="cell c-testing"><svg class="tick"><use href="#tick"/></svg></div>
    <div class="label">PSHYSCOLOGY</div><div class="cell"></div><div class="cell c-mental"><svg class="tick"><use href="#tick"/></svg></div><div class="cell"></div><div class="cell"></div><div class="cell"></div><div class="cell"></div><div class="cell"></div>
    <div class="label">MINDFULLNESS<br>MEDITATION</div><div class="cell"></div><div class="cell c-mental"><svg class="tick"><use href="#tick"/></svg></div><div class="cell"></div><div class="cell"></div><div class="cell"></div><div class="cell"></div><div class="cell"></div>
    <div class="label">LIFE<br>COACHING</div><div class="cell"></div><div class="cell c-mental"><svg class="tick"><use href="#tick"/></svg></div><div class="cell"></div><div class="cell"></div><div class="cell"></div><div class="cell"></div><div class="cell"></div>
    <div class="label">NLP</div><div class="cell"></div><div class="cell c-mental"><svg class="tick"><use href="#tick"/></svg></div><div class="cell"></div><div class="cell"></div><div class="cell c-subconscious"><svg class="tick"><use href="#tick"/></svg></div><div class="cell"></div><div class="cell c-testing"><svg class="tick"><use href="#tick"/></svg></div>
    <div class="label">REIKI</div><div class="cell"></div><div class="cell"></div><div class="cell"></div><div class="cell c-energetic"><svg class="tick"><use href="#tick"/></svg></div><div class="cell"></div><div class="cell"></div><div class="cell"></div>
    <div class="label">CRYSTAL<br>HEALING</div><div class="cell"></div><div class="cell"></div><div class="cell"></div><div class="cell c-energetic"><svg class="tick"><use href="#tick"/></svg></div><div class="cell"></div><div class="cell"></div><div class="cell"></div>
    <div class="label">BOWEN<br>THERAPY</div><div class="cell c-physical"><svg class="tick"><use href="#tick"/></svg></div><div class="cell"></div><div class="cell"></div><div class="cell"></div><div class="cell c-subconscious"><svg class="tick"><use href="#tick"/></svg></div><div class="cell"></div><div class="cell c-testing"><svg class="tick"><use href="#tick"/></svg></div>
    <div class="label">ENERGY<br>MEDICINE</div><div class="cell"></div><div class="cell"></div><div class="cell"></div><div class="cell c-energetic"><svg class="tick"><use href="#tick"/></svg></div><div class="cell"></div><div class="cell"></div><div class="cell c-testing"><svg class="tick"><use href="#tick"/></svg></div>
    <div class="label">HYPNOTHERAPY</div><div class="cell"></div><div class="cell c-mental"><svg class="tick"><use href="#tick"/></svg></div><div class="cell"></div><div class="cell"></div><div class="cell c-subconscious"><svg class="tick"><use href="#tick"/></svg></div><div class="cell"></div><div class="cell"></div>
    <div class="label">ACUPUNCTURE</div><div class="cell c-physical"><svg class="tick"><use href="#tick"/></svg></div><div class="cell"></div><div class="cell"></div><div class="cell c-energetic"><svg class="tick"><use href="#tick"/></svg></div><div class="cell"></div><div class="cell"></div><div class="cell"></div>
    <div class="label">TIMELINE<br>THERAPY</div><div class="cell"></div><div class="cell c-mental"><svg class="tick"><use href="#tick"/></svg></div><div class="cell"></div><div class="cell"></div><div class="cell c-subconscious"><svg class="tick"><use href="#tick"/></svg></div><div class="cell"></div><div class="cell c-testing"><svg class="tick"><use href="#tick"/></svg></div>
    <div class="label">INNER CHILD<br>HEALING</div><div class="cell"></div><div class="cell c-mental"><svg class="tick"><use href="#tick"/></svg></div><div class="cell"></div><div class="cell"></div><div class="cell c-subconscious"><svg class="tick"><use href="#tick"/></svg></div><div class="cell"></div><div class="cell"></div>
    <div class="label">THETA<br>HEALING</div><div class="cell"></div><div class="cell"></div><div class="cell"></div><div class="cell"></div><div class="cell c-subconscious"><svg class="tick"><use href="#tick"/></svg></div><div class="cell c-superconscious"><svg class="tick"><use href="#tick"/></svg></div><div class="cell"></div>
    <div class="label">EFT</div><div class="cell c-physical"><svg class="tick"><use href="#tick"/></svg></div><div class="cell c-mental"><svg class="tick"><use href="#tick"/></svg></div><div class="cell"></div><div class="cell"></div><div class="cell c-subconscious"><svg class="tick"><use href="#tick"/></svg></div><div class="cell"></div><div class="cell c-testing"><svg class="tick"><use href="#tick"/></svg></div>
    <div class="label">FAMILY<br>CONSTELLATION</div><div class="cell c-physical"><svg class="tick"><use href="#tick"/></svg></div><div class="cell c-mental"><svg class="tick"><use href="#tick"/></svg></div><div class="cell"></div><div class="cell c-energetic"><svg class="tick"><use href="#tick"/></svg></div><div class="cell"></div><div class="cell"></div><div class="cell"></div>
    <div class="label">PSYCHIC<br>INTUITIVE</div><div class="cell c-physical"><svg class="tick"><use href="#tick"/></svg></div><div class="cell c-mental"><svg class="tick"><use href="#tick"/></svg></div><div class="cell"></div><div class="cell"></div><div class="cell"></div><div class="cell"></div><div class="cell"></div>
    <div class="label">AYURVEDIC<br>MEDICINE</div><div class="cell c-physical"><svg class="tick"><use href="#tick"/></svg></div><div class="cell"></div><div class="cell"></div><div class="cell"></div><div class="cell"></div><div class="cell"></div><div class="cell"></div>
    <div class="label">WESTERN<br>MEDICINE</div><div class="cell c-physical"><svg class="tick"><use href="#tick"/></svg></div><div class="cell"></div><div class="cell"></div><div class="cell"></div><div class="cell"></div><div class="cell"></div><div class="cell"></div>
  </div>

  <div class="feature">
    <div class="feature-label">KRV</div>
    <div class="cell c-physical"><svg class="tick"><use href="#tick"/></svg></div>
    <div class="cell c-mental"><svg class="tick"><use href="#tick"/></svg></div>
    <div class="cell c-emotional"><svg class="tick"><use href="#tick"/></svg></div>
    <div class="cell c-energetic"><svg class="tick"><use href="#tick"/></svg></div>
    <div class="cell c-subconscious"><svg class="tick"><use href="#tick"/></svg></div>
    <div class="cell c-superconscious"><svg class="tick"><use href="#tick"/></svg></div>
    <div class="cell c-testing"><svg class="tick"><use href="#tick"/></svg></div>
  </div>
</section>

<section class="notes">
  <div class="note n-physical" style="left:60px;top:1696px">
    <h3>PHYSICAL</h3>
    <p>Most modalities, including, a western medicine, focus on and treat the physical body only. The KRV process enables you to engage in healing your own body during the session. There is no muscle testing, no hands-on healing and no herbal remedies or medicines.</p>
  </div>
  <div class="note n-mental" style="left:60px;top:1856px">
    <h3>MENTAL</h3>
    <p>KRV enables you to use your own consciousness to self-heal.<br>We don't give you advice or coaching, we allow your mind to heal itself.</p>
  </div>
  <div class="note n-emotional" style="left:60px;top:2008px">
    <h3>EMOTIONAL</h3>
    <p>KRV is the only modality that engages your emotions on a physical level. Emotions get stuck in your body and can cause illness over time if left unchecked. KRV enables you to experience fast and powerful emotional releasing.</p>
  </div>
  <div class="note n-energetic" style="left:668px;top:1696px">
    <h3>ENERGETIC</h3>
    <p>Most modalities try to move the energy in your body for you. KRV enables and empowers you to do it yourself.</p>
  </div>
  <div class="note n-subconscious" style="left:668px;top:1796px">
    <h3>SUBCONSCIOUS</h3>
    <p>Some modalities, like Kinesiology, access your subconscious through muscle testing. KRV empowers you to access your own subconscious and heal it yourself.</p>
  </div>
  <div class="note n-superconscious" style="left:668px;top:1926px">
    <h3>SUPERCONSCIOUS</h3>
    <p>KRV is the only modality that enables you to access and heal your superconscious mind yourself.</p>
  </div>
  <div class="note n-testing" style="left:668px;top:2052px">
    <h3>BEFORE &amp; AFTER TESTING</h3>
    <p>KRV is the only modality that enables you to provide before and after results, which are documented by US, and analysed by you with our help.</p>
  </div>
</section>

<footer class="footer">
  <div class="footer-brand"><span class="footer-dot"></span>Lumina</div>
  <div class="footer-url">www.luminaworks.com.au</div>
</footer>
</body>
</html>
```